Corrindale Planners, LLC Stationary

Corrindale Planners, LLC is a new financial planning and consulting company. We are looking for designs on business cards, letterhead, envelopes, and anything else that would be useful. Our preference for business card design is two sided. We are looking for a professional and clean look with incorporating the logo and patriotic feel. Thank you to all who participate and good luck!

```html
<!DOCTYPE html>
<html lang="en">
<head>
<meta charset="utf-8">
<title>Corrindale Planners, LLC Stationery</title>
<link href="https://fonts.googleapis.com/css2?family=Open+Sans:wght@400;600;700&display=swap" rel="stylesheet">
<style>
  :root {
    --navy: #1c3f6e;
    --red: #d8141f;
    --red-deep: #a3131a;
    --paper: #ffffff;
    --ink: #555b63;
    --rule: #d6d9de;
    --backdrop: #e6e6e6;
    --card-back-text: #fbe3e4;
  }
  * { box-sizing: border-box; margin: 0; padding: 0; }
  html, body { width: 1200px; height: 1200px; overflow: hidden; }
  body {
    position: relative;
    font-family: "Open Sans", Arial, sans-serif;
    background: var(--backdrop);
    color: var(--ink);
  }
  .sheet {
    position: absolute;
    background: var(--paper);
    box-shadow: 0 2px 6px rgba(0,0,0,0.12);
  }
  .brand { display: flex; align-items: flex-start; gap: 8px; }
  .brand-square { width: 14px; height: 14px; background: var(--navy); margin-top: 5px; flex: none; }
  .brand-name {
    font-weight: 700;
    color: var(--navy);
    letter-spacing: 0.02em;
    line-height: 1.2;
    white-space: nowrap;
  }
  .brand-tagline {
    font-size: 7px;
    letter-spacing: 0.12em;
    text-transform: uppercase;
    color: var(--navy);
    margin-top: 3px;
    white-space: nowrap;
  }

  /* Letterhead */
  .letterhead { left: 50px; top: 280px; width: 500px; height: 647px; }
  .letterhead .brand { position: absolute; right: 36px; top: 36px; }
  .letterhead .brand-name { font-size: 18px; }
  .letterhead .contact {
    position: absolute; right: 36px; top: 96px;
    text-align: right; font-size: 11px; line-height: 1.5;
  }
  .letterhead .contact .gap { height: 10px; }

  /* Envelope */
  .envelope { left: 590px; top: 280px; width: 560px; height: 243px; }
  .envelope .brand { position: absolute; left: 32px; top: 30px; }
  .envelope .brand-name { font-size: 18px; }
  .envelope .address {
    position: absolute; left: 32px; bottom: 24px;
    font-size: 10px; letter-spacing: 0.06em;
  }

  /* Business cards */
  .card { width: 270px; height: 154px; overflow: hidden; top: 553px; }
  .card-front { left: 590px; }
  .card-back { left: 880px; background: linear-gradient(135deg, var(--red) 0%, var(--red-deep) 100%); }
  .card-front .corner { position: absolute; right: 0; top: 0; width: 90px; height: 154px; }
  .card-front .person { position: absolute; left: 14px; top: 16px; }
  .card-front .person-name { font-size: 11px; font-weight: 700; color: var(--red); text-transform: uppercase; letter-spacing: 0.03em; }
  .card-front .person-role { font-size: 7px; }
  .card-front .details { position: absolute; left: 14px; top: 52px; font-size: 7px; line-height: 1.5; }
  .card-front .details b { color: var(--red); font-weight: 600; }
  .card-front .divider { position: absolute; left: 14px; top: 105px; width: 160px; height: 1px; background: var(--rule); }
  .card-front .brand { position: absolute; left: 14px; top: 113px; gap: 6px; }
  .card-front .brand-square { width: 9px; height: 9px; margin-top: 3px; }
  .card-front .brand-name { font-size: 11px; }
  .card-front .brand-tagline { font-size: 5px; }
  .card-back .address {
    position: absolute; left: 14px; bottom: 14px;
    font-size: 7px; line-height: 1.5; color: var(--card-back-text);
  }
</style>
</head>
<body>

  <section class="sheet letterhead" aria-label="Letterhead">
    <div class="brand">
      <div>
        <div class="brand-name">Corrindale Planners, LLC</div>
        <div class="brand-tagline">Financial Planning and Consulting</div>
      </div>
      <span class="brand-square"></span>
    </div>
    <div class="contact">
      <div>+01 40213 7745</div>
      <div>www.corrindaleplanners.com</div>
      <div>info@corrindaleplanners.com</div>
      <div class="gap"></div>
      <div>Dummy City</div>
      <div>Dummy Country, Dummy State</div>
    </div>
  </section>

  <section class="sheet envelope" aria-label="Envelope">
    <div class="brand">
      <span class="brand-square"></span>
      <div>
        <div class="brand-name">Corrindale Planners, LLC</div>
        <div class="brand-tagline">Financial Planning and Consulting</div>
      </div>
    </div>
    <div class="address">Dummy City, Dummy Country, Dummy State</div>
  </section>

  <section class="sheet card card-front" aria-label="Business card front">
    <svg class="corner" viewBox="0 0 90 154" aria-hidden="true">
      <polygon points="0,0 90,0 90,30" fill="var(--red)"/>
      <polygon points="90,40 90,154 40,154" fill="var(--navy)"/>
    </svg>
    <div class="person">
      <div class="person-name">John Doe</div>
      <div class="person-role">Director</div>
    </div>
    <div class="details">
      <div><b>M.</b> +01 3308 61924</div>
      <div><b>T.</b> +01 40213 7745</div>
      <div>www.corrindaleplanners.com</div>
      <div>john@corrindaleplanners.com</div>
    </div>
    <div class="divider"></div>
    <div class="brand">
      <span class="brand-square"></span>
      <div>
        <div class="brand-name">Corrindale Planners, LLC</div>
        <div class="brand-tagline">Financial Planning and Consulting</div>
      </div>
    </div>
  </section>

  <section class="sheet card card-back" aria-label="Business card back">
    <div class="address">
      <div>Dummy City</div>
      <div>Dummy Country, Dummy State</div>
    </div>
  </section>

</body>
</html>
```